business card design for a plumbing contractor

i need a double business card for a plumbing business, our initial service is residential Sewer Drain Cleaning.

Target Market(s)

other plumbing Business

Industry/Entity Type

Plumbing

Contact Information for Business Card

www.PipeworksCrestline.example- 5817302946-

Font styles to use
Serif

Colors
ec1f27
0455a3

```html
<!DOCTYPE html>
<html lang="en">
<head>
<meta charset="utf-8">
<title>Pipeworks Crestline — Business Card</title>
<link rel="stylesheet" href="https://fonts.googleapis.com/css2?family=Signika:wght@400;600&family=Roboto:wght@400&display=swap">
<style>
  :root {
    --backdrop: #2a2a2a;
    --card-white: #f2f2f2;
    --brand-red: #d63a30;
    --name-red: #d63a30;
    --title-taupe: #8a7c6c;
    --contact-grey: #555555;
    --on-red: #ffffff;
  }
  * { margin: 0; padding: 0; box-sizing: border-box; }
  html, body {
    width: 1200px; height: 960px; overflow: hidden;
    background: var(--backdrop);
  }
  .canvas { position: relative; width: 1200px; height: 960px; }
  .card {
    position: absolute; width: 600px; height: 342px;
    display: flex; flex-direction: column; align-items: center;
  }
  .card--front { left: 322px; top: 108px; background: var(--card-white); }
  .card--back { left: 320px; top: 493px; background: var(--brand-red); }

  .front-brand {
    margin-top: 112px;
    display: flex; align-items: center; gap: 8px;
    font-family: "Signika", sans-serif; font-weight: 600;
    font-size: 26px; color: var(--brand-red); line-height: 1;
  }
  .front-brand .mark { width: 14px; height: 14px; background: var(--brand-red); }
  .person {
    margin-top: 52px;
    font-family: "Signika", sans-serif; font-weight: 600; line-height: 1;
  }
  .person .name { font-size: 21px; color: var(--name-red); text-transform: uppercase; }
  .person .role { font-size: 16px; color: var(--title-taupe); text-transform: uppercase; }
  .contact {
    margin-top: 9px;
    font-family: "Signika", sans-serif; font-weight: 600;
    font-size: 15px; line-height: 20px; color: var(--contact-grey);
    text-align: center;
  }

  .back-brand {
    margin-top: 138px;
    font-family: "Signika", sans-serif; font-weight: 600;
    font-size: 44px; line-height: 1; color: var(--on-red);
  }
  .services {
    margin-top: 96px;
    font-family: "Roboto", sans-serif; font-size: 15px; color: var(--on-red);
  }
</style>
</head>
<body>
<main class="canvas">
  <section class="card card--front">
    <div class="front-brand"><span class="mark"></span>Pipeworks Crestline</div>
    <p class="person"><span class="name">Dana Whitfield -</span> <span class="role">CEO/Founder</span></p>
    <p class="contact">P.5817302946| Dispatcher@PipeworksCrestline.example<br>www.PipeworksCrestline.example</p>
  </section>

  <section class="card card--back">
    <div class="back-brand">Pipeworks Crestline</div>
    <p class="services">Sewer Drain Cleaning • Maintenance • Trenchless Pipe Installs</p>
  </section>
</main>
</body>
</html>
```